IT Consultancy Website Redesign

We would like to redesign our current website.

We have an overall look/feel we like based on a rendering we have for our homepage. (Attached)

Pages that need to be designed (11 total):

-Homepage

-Overview (not it's own page just a navigation header/drop down title)
-About Us
-Why Choose Vorniq
-Our Approach

-Insights (not it's own page just a navigation header/drop down title)
-Insights (Blog)
-Case Studies
-Events

-Services (not it's own page just a navigation header/drop down title)
- Run-State Support

-Industries
-Legal

-Careers
-Contact page

If you have any questions please ask.

Target Market(s)

Meridale 500 C-suite executives

Industry/Entity Type

It Company

Coding

Coded - Design and coding required

Number of Pages Required

5+ page

Font styles to use
Serif
Sans Serif

Requirements
Must have
• Pages must closely resemble the example provided

```html
<!DOCTYPE html>
<html lang="en">
<head>
<meta charset="utf-8">
<title>Vorniq – IT Strategy and Implementation</title>
<link href="https://fonts.googleapis.com/css2?family=Open+Sans:wght@400;600;700;800&display=swap" rel="stylesheet">
<style>
:root{
  --red:#e0262b;
  --red-soft:#f3a9ab;
  --ink:#1b1b1b;
  --text:#555;
  --muted:#888;
  --dark:#1c1c1c;
  --darker:#121212;
  --line:#e6e6e6;
  --white:#fff;
}
*{box-sizing:border-box;margin:0;padding:0}
html,body{width:1200px;height:3748px;overflow:hidden}
body{position:relative;background:var(--white);font-family:"Open Sans",Arial,sans-serif;color:var(--ink)}
.abs{position:absolute}
.btn{display:inline-block;font-size:10px;font-weight:700;color:var(--white);background:var(--red);padding:7px 16px;border-radius:2px}
.btn-dark{background:var(--ink)}
.photo{position:absolute}
p{font-size:12px;line-height:1.7;color:var(--text)}

/* header */
.site-header{position:absolute;left:0;top:0;width:1200px;height:48px;background:var(--white);box-shadow:0 1px 4px rgba(0,0,0,.08);z-index:5}
.brand{position:absolute;left:210px;top:12px;display:flex;align-items:center;gap:8px;font-size:20px;font-weight:800;letter-spacing:1px;color:var(--ink)}
.brand .mark{width:12px;height:12px;background:var(--red)}
.main-nav{position:absolute;right:80px;top:14px;display:flex;gap:30px;align-items:center;font-size:10px;font-weight:700;color:var(--ink)}

/* hero */
.hero{position:absolute;left:0;top:48px;width:1200px;height:472px;background:linear-gradient(120deg,#2b2d31 0%,#3c3f45 45%,#24262a 100%);overflow:hidden}
.hero-photo{left:640px;top:40px;width:500px;height:400px;background:linear-gradient(135deg,#cfd3d8,#7e848c);clip-path:polygon(18% 0,100% 0,100% 100%,0 100%)}
.hero-title{left:210px;top:150px;font-size:40px;font-weight:800;line-height:1.15;color:var(--white)}
.hero-title span{color:var(--red)}
.hero-text{left:210px;top:258px;width:300px;color:#d7d7d7;font-size:11px}
.hero-cta{left:210px;top:312px}
.hero-dots{left:210px;top:432px;display:flex;gap:8px}
.hero-dots i{width:8px;height:8px;border-radius:50%;background:rgba(255,255,255,.45)}
.hero-dots i:first-child{background:var(--red)}
.social{right:60px;top:420px;display:flex;gap:6px}
.social i{width:20px;height:20px;border:1px solid rgba(255,255,255,.7)}

/* empower */
.empower-title{left:210px;top:650px;font-size:26px;font-weight:800;line-height:1.2}
.empower-text{left:210px;top:728px;width:300px;font-size:10px}
.empower-cta{left:210px;top:800px}
.empower-photo{left:590px;top:596px;width:270px;height:280px;background:linear-gradient(135deg,#c9ccd1,#6f757d)}

/* help */
.help-title{left:210px;top:945px;font-size:26px;font-weight:800;line-height:1.2}
.help-text{left:620px;top:948px;width:380px;font-size:10px}
.help-text b{color:var(--ink)}
.help-arrows{left:1050px;top:1050px;display:flex;gap:10px}
.help-arrows i{width:14px;height:2px;background:var(--red)}
.help-photo{left:60px;top:1068px;width:460px;height:292px;background:linear-gradient(135deg,#b8bcc1,#6a6f76)}
.service-card{position:absolute;top:1128px;width:172px;height:226px;background:var(--white);box-shadow:0 4px 16px rgba(0,0,0,.14);padding:22px 16px}
.service-card.featured{background:var(--red);color:var(--white)}
.service-card h3{font-size:12px;font-weight:700;margin:14px 0 6px}
.service-card p{font-size:9px;line-height:1.6}
.service-card.featured p{color:#fde3e3}
.service-card .more{display:block;margin-top:10px;font-size:9px;font-weight:700;color:var(--red)}
.service-card.featured .more{color:var(--white)}

/* features */
.center-head{position:absolute;left:0;width:1200px;text-align:center}
.center-head h2{font-size:22px;font-weight:800}
.center-head p{font-size:10px;margin-top:14px}
.feature{position:absolute;top:1600px;width:260px;height:328px;text-align:center;padding-top:60px}
.feature.boxed{border:1px solid var(--red-soft);border-radius:4px;background:var(--white)}
.feature h3{font-size:14px;font-weight:700;margin:22px 0 10px;line-height:1.4}
.feature p{font-size:9px;width:190px;margin:0 auto}

/* featured product */
.featured-photo{left:208px;top:1980px;width:944px;height:340px;background:linear-gradient(120deg,#a8977f,#6e6358 55%,#3e3a36)}
.featured-box{position:absolute;left:208px;top:2020px;width:372px;height:260px;background:var(--red);padding:36px 36px}
.featured-box h2{font-size:40px;font-weight:800;line-height:1.05;color:var(--white)}
.featured-box p{color:#fde3e3;font-size:10px;margin:16px 0 18px;width:260px}

/* industries */
.industry{position:absolute;top:2512px;height:268px}
.industry-label{position:absolute;left:460px;top:2580px;width:268px;height:150px;background:rgba(224,38,43,.85);display:flex;align-items:center;justify-content:center;color:var(--white);font-size:18px;font-weight:700}
.dots{position:absolute;left:0;width:1200px;display:flex;justify-content:center;gap:8px}
.dots i{width:8px;height:8px;border-radius:50%;background:var(--red)}

/* blog */
.blog-card{position:absolute;background:var(--white);box-shadow:0 4px 18px rgba(0,0,0,.12)}
.blog-card .thumb{height:150px;background:linear-gradient(135deg,#d8dadd,#8b9097)}
.blog-card .body{padding:14px 16px}
.blog-card .meta{display:flex;align-items:center;gap:6px;font-size:9px;color:var(--muted)}
.blog-card .meta i{width:8px;height:8px;border-radius:50%;background:var(--red)}
.blog-card h3{font-size:12px;font-weight:700;margin:8px 0 6px;line-height:1.35}
.blog-card p{font-size:9px;line-height:1.6;margin-bottom:12px}
.blog-card.lead .meta{color:var(--red)}

/* newsletter + footer */
.newsletter{position:absolute;left:0;top:3430px;width:1200px;height:42px;background:var(--dark)}
.newsletter .strip{position:absolute;left:0;top:0;width:470px;height:42px;background:var(--red);display:flex;align-items:center;gap:10px;padding-left:210px;color:var(--white);font-size:9px}
.newsletter .strip b{font-size:12px;font-weight:800}
.field{position:absolute;top:11px;height:20px;border:1px solid #666;font-size:9px;color:#aaa;padding:3px 8px}
.join{position:absolute;left:1020px;top:10px;padding:5px 16px}
.site-footer{position:absolute;left:0;top:3472px;width:1200px;height:276px;background:var(--darker);color:#ccc}
.footer-brand{left:210px;top:48px;color:var(--white)}
.footer-nav{position:absolute;right:80px;top:66px;display:flex;gap:30px;font-size:10px;font-weight:700;color:#ddd}
.footer-rule{position:absolute;left:210px;top:110px;width:910px;height:1px;background:#333}
.contact{position:absolute;top:136px;font-size:11px;line-height:1.7}
.contact h4{display:flex;align-items:center;gap:8px;font-size:10px;font-weight:700;color:var(--white)}
</style>
</head>
<body>

<header class="site-header">
  <div class="brand"><span class="mark"></span>VORNIQ</div>
  <nav class="main-nav">
    <span>OVERVIEW</span><span>OUR FOCUS</span><span>INDUSTRIES</span><span>CAREERS</span>
    <span class="btn">GET IN TOUCH</span>
  </nav>
</header>

<section class="hero">
  <div class="photo hero-photo" role="img" aria-label="Team of consultants working around a conference table"></div>
  <svg class="abs" style="left:600px;top:0" width="600" height="472" viewBox="0 0 600 472">
    <polygon points="120,472 260,120 320,472" fill="#e0262b"/>
    <polygon points="420,0 600,0 600,200" fill="#e0262b" opacity=".9"/>
  </svg>
  <h1 class="abs hero-title">IT Strategy and<br><span>Implementation</span></h1>
  <p class="abs hero-text">We take your company to the cutting edge of efficiency.</p>
  <span class="abs btn hero-cta">Learn More</span>
  <div class="abs hero-dots"><i></i><i></i><i></i></div>
  <div class="abs social"><i></i><i></i><i></i><i></i></div>
</section>

<section class="empower">
  <h2 class="abs empower-title">Empower Digital<br>Transformation</h2>
  <p class="abs empower-text">Vorniq Solutions is a team of IT experts who understand the IT field and its constant shifts. From consultancy to implementation we can help you identify the best solution for your company.</p>
  <span class="abs btn empower-cta">Learn More</span>
  <svg class="abs" style="left:770px;top:590px" width="330" height="300" viewBox="0 0 330 300">
    <polygon points="160,8 322,292 10,292" fill="none" stroke="#f3a9ab" stroke-width="22"/>
  </svg>
  <div class="photo empower-photo" role="img" aria-label="Business professionals in a meeting"></div>
</section>

<section class="help">
  <h2 class="abs help-title">Here's how<br>we Help you</h2>
  <p class="abs help-text">Lorem ipsum dolor sit amet, consectetur adipiscing elit sed do eiusmod tempor incididunt ut labore et dolore magna aliqua. <b>Quis ipsum sus pendisse ultrices gravida.</b></p>
  <div class="abs help-arrows"><i></i><i></i></div>
  <div class="photo help-photo" role="img" aria-label="Colleagues collaborating in an office"></div>

  <article class="service-card" style="left:484px">
    <svg width="28" height="24" viewBox="0 0 28 24"><rect x="2" y="2" width="24" height="15" fill="none" stroke="#1b1b1b" stroke-width="2"/><path d="M9 22h10M14 17v5" stroke="#1b1b1b" stroke-width="2"/></svg>
    <h3>Manage Service</h3>
    <p>Lorem ipsum dolor sit amet, consectetur adipi cing elit sed do eiusmod.</p>
    <span class="more">Read More</span>
  </article>
  <article class="service-card featured" style="left:664px;top:1108px;height:246px">
    <svg width="28" height="24" viewBox="0 0 28 24"><rect x="2" y="2" width="24" height="15" fill="none" stroke="#fff" stroke-width="2"/><path d="M9 22h10M14 17v5M10 10l3 3 5-6" stroke="#fff" stroke-width="2" fill="none"/></svg>
    <h3>Implementation Service</h3>
    <p>Lorem ipsum dolor sit amet, consectetur adipi cing elit sed do eiusmod.</p>
    <span class="more">Read More</span>
  </article>
  <article class="service-card" style="left:846px">
    <svg width="28" height="24" viewBox="0 0 28 24"><rect x="2" y="2" width="24" height="15" fill="none" stroke="#1b1b1b" stroke-width="2"/><path d="M9 22h10M14 17v5" stroke="#1b1b1b" stroke-width="2"/></svg>
    <h3>Virtual Assistance</h3>
    <p>Lorem ipsum dolor sit amet, consectetur adipi cing elit sed do eiusmod.</p>
    <span class="more">Read More</span>
  </article>
</section>

<section class="features">
  <div class="center-head" style="top:1448px">
    <h2>Consectetur adipiscing</h2>
    <p>Lorem ipsum dolor sit amet, consectetur adipiscing elit,<br>sed do eiusm ut labore et dolore magna aliqua.</p>
  </div>
  <div class="feature" style="left:186px">
    <svg width="40" height="36" viewBox="0 0 40 36"><path d="M4 14l10-8 8 6 8-6 6 8-14 14z" fill="none" stroke="#e0262b" stroke-width="2"/></svg>
    <h3>Superior Service<br>Quality</h3>
    <p>Our Customer Centric Pool and crews stand in truly as 99% prove it</p>
  </div>
  <div class="feature boxed" style="left:452px">
    <svg width="40" height="36" viewBox="0 0 40 36"><circle cx="20" cy="18" r="8" fill="none" stroke="#e0262b" stroke-width="2"/><path d="M20 4v6M20 26v6M6 18h6M28 18h6" stroke="#e0262b" stroke-width="2"/></svg>
    <h3>Experienced Solution<br>Developers</h3>
    <p>All of our Developer have vast experience in the latest solutions and tools</p>
  </div>
  <div class="feature" style="left:716px">
    <svg width="40" height="36" viewBox="0 0 40 36"><path d="M12 4h16v10a8 8 0 0 1-16 0zM12 8H6a6 6 0 0 0 6 8M28 8h6a6 6 0 0 1-6 8M20 22v6M13 32h14" fill="none" stroke="#e0262b" stroke-width="2"/></svg>
    <h3>Competitive<br>Pricing</h3>
    <p>All solution are presented with price at delivery, optimizing full time as Developer a plan of it</p>
  </div>
</section>

<section class="featured">
  <div class="photo featured-photo" role="img" aria-label="Team working on laptops around a shared desk"></div>
  <div class="featured-box">
    <h2>FEATURED<br>PRODUCT</h2>
    <p>Lorem ipsum dolor sit amet, conse ctetur adipiscing elit, sed do eiusmod.</p>
    <span class="btn btn-dark">Learn More</span>
  </div>
</section>

<section class="industries">
  <div class="center-head" style="top:2392px">
    <h2>Industries</h2>
    <p>Lorem ipsum dolor sit amet, consectetur adipiscing elit,<br>sed do eiusm ut labore et dolore magna aliqua.</p>
  </div>
  <div class="industry" style="left:60px;width:340px;background:linear-gradient(135deg,#c7c7c7,#6c6c6c)" role="img" aria-label="Black and white photo of a legal team meeting"></div>
  <div class="industry" style="left:408px;width:372px;background:linear-gradient(135deg,#9a8f86,#4f4a46)" role="img" aria-label="Black and white photo of factory equipment"></div>
  <div class="industry" style="left:788px;width:364px;background:linear-gradient(135deg,#cfcfcf,#737373)" role="img" aria-label="Black and white photo of healthcare professionals"></div>
  <div class="industry-label">Manufacturing</div>
  <div class="dots" style="top:2816px"><i></i><i></i><i></i></div>
</section>

<section class="blog">
  <div class="center-head" style="top:2896px"><h2>Our Blog</h2></div>
  <article class="blog-card" style="left:204px;top:3004px;width:236px">
    <div class="thumb" role="img" aria-label="Consultants reviewing documents"></div>
    <div class="body">
      <div class="meta"><i></i>Lorem Ipsum</div>
      <h3>Lorem ipsum dolor sit amet, consectetur adipiscing elit</h3>
      <p>Sed do eiusmod tempor incididunt ut labore et dolore magna aliqua.</p>
      <span class="btn btn-dark">Learn More</span>
    </div>
  </article>
  <article class="blog-card lead" style="left:470px;top:2964px;width:270px">
    <div class="thumb" style="height:180px" role="img" aria-label="Presenter at a whiteboard with colleagues"></div>
    <div class="body">
      <div class="meta"><i></i>Lorem Ipsum</div>
      <h3>Lorem ipsum dolor sit amet, consectetur adipiscing elit</h3>
      <p>Sed do eiusmod tempor incididunt ut labore et dolore magna aliqua.</p>
      <span class="btn">Learn More</span>
    </div>
  </article>
  <article class="blog-card" style="left:770px;top:3004px;width:236px">
    <div class="thumb" role="img" aria-label="Team discussion in a bright office"></div>
    <div class="body">
      <div class="meta"><i></i>Lorem Ipsum</div>
      <h3>Lorem ipsum dolor sit amet, consectetur adipiscing elit</h3>
      <p>Sed do eiusmod tempor incididunt ut labore et dolore magna aliqua.</p>
      <span class="btn btn-dark">Learn More</span>
    </div>
  </article>
</section>

<section class="newsletter">
  <div class="strip"><b>JOIN VORNIQ</b>Lorem ipsum dolor sit amet consectetur</div>
  <span class="field" style="left:720px;width:150px">Your Name</span>
  <span class="field" style="left:880px;width:126px">Email Id</span>
  <span class="btn join">Join Now</span>
</section>

<footer class="site-footer">
  <div class="abs brand footer-brand"><span class="mark"></span>VORNIQ</div>
  <nav class="footer-nav"><span>OVERVIEW</span><span>OUR FOCUS</span><span>INDUSTRIES</span><span>BLOG</span><span>CAREERS</span></nav>
  <div class="footer-rule"></div>
  <div class="contact" style="left:210px">
    <h4><svg width="12" height="12" viewBox="0 0 12 12"><path d="M2 1h3l1 3-2 1a7 7 0 0 0 3 3l1-2 3 1v3a1 1 0 0 1-1 1A10 10 0 0 1 1 2a1 1 0 0 1 1-1z" fill="#e0262b"/></svg>PHONE</h4>
    555-014-2290
  </div>
  <div class="contact" style="left:480px">
    <h4><svg width="12" height="12" viewBox="0 0 12 12"><rect x="1" y="2.5" width="10" height="7" fill="none" stroke="#e0262b" stroke-width="1.4"/><path d="M1 3l5 4 5-4" fill="none" stroke="#e0262b" stroke-width="1.4"/></svg>EMAIL</h4>
    INFO@VORNIQSOLUTIONS.COM
  </div>
  <div class="contact" style="left:820px">
    <h4><svg width="12" height="12" viewBox="0 0 12 12"><path d="M6 11S2 7 2 4.5a4 4 0 0 1 8 0C10 7 6 11 6 11z" fill="#e0262b"/><circle cx="6" cy="4.5" r="1.4" fill="#121212"/></svg>ADDRESS</h4>
    418 HARBOR LANE, SUITE 210<br>EASTBROOK
  </div>
</footer>

</body>
</html>
```